Used Car Dealer seeks an Amazing Business Card Design

We are looking for a business card design that incorporates our logo and grabs the attention of anyone we give the business card to.

Looking to use the same colors as the logo. Our Logo choice is the black background with Red and Silver/Grey Lettering.

We also would like to see some embossed designs.

Target Market(s)

Used Car Buyers, Automotive, Auto

Industry/Entity Type

Automotive

Contact Information for Business Card

BVEL7K
Gordon Whitlock
482 Tarrow Lane
Suite 207
Larkfield, GA 30419
Office (770) 555-0142
Cell (770) 555-0187
bvel7kga@quellmail.com
www.bvel7kga.com

Colors
ffffff
ee3036

Requirements
Must have
• Must include our logo (Black Background with Red and Silver/Grey Lettering)
Nice to have
• Embossed Design. Can be Single or Double Sided.

```html
<!DOCTYPE html>
<html lang="en">
<head>
<meta charset="utf-8">
<title>BVEL7K Business Card</title>
<link rel="stylesheet" href="https://fonts.googleapis.com/css2?family=Source+Sans+3:wght@400;600;700&display=swap">
<style>
  :root {
    --red-bright: #f50000;
    --red-mid: #e00000;
    --red-deep: #b80000;
    --black: #000000;
    --rule: #e4e4e4;
    --white: #ffffff;
    --silver: #d8d8d8;
    --backdrop: #eeeae6;
  }
  * { margin: 0; padding: 0; box-sizing: border-box; }
  html, body { width: 1200px; height: 900px; overflow: hidden; background: var(--backdrop); }
  body { font-family: "Source Sans 3", "Myriad Pro", Arial, sans-serif; position: relative; }

  .card {
    position: absolute;
    display: flex;
    flex-direction: column;
    box-shadow: 0 6px 18px rgba(0,0,0,0.18);
    overflow: hidden;
  }
  .card--front { left: 78px; top: 34px; width: 587px; height: 364px; }
  .card--back { left: 388px; top: 505px; width: 567px; height: 352px; }

  .band-top { background: linear-gradient(180deg, var(--red-bright), var(--red-mid)); }
  .band-bottom { background: linear-gradient(180deg, var(--red-mid), var(--red-deep)); }
  .rule { height: 7px; background: var(--rule); }
  .panel { background: var(--black); position: relative; color: var(--white); }

  .card--front .band-top { height: 94px; }
  .card--front .panel { height: 180px; }
  .card--front .band-bottom { flex: 1; }

  .card--back .band-top { height: 86px; }
  .card--back .panel { height: 162px; display: flex; align-items: center; justify-content: center; }
  .card--back .band-bottom { flex: 1; display: flex; align-items: center; justify-content: center; padding-top: 8px; }

  .holder { position: absolute; left: 28px; top: 39px; }
  .holder-name { font-size: 22px; font-weight: 600; line-height: 1; margin-bottom: 19px; }
  .holder-address { font-size: 16.5px; line-height: 24px; }

  .contact-list { position: absolute; right: 30px; top: 57px; list-style: none; }
  .contact-item {
    display: flex; align-items: center; justify-content: flex-end;
    font-size: 15.5px; line-height: 24.5px; gap: 8px;
  }
  .contact-icon { width: 13px; height: 13px; fill: var(--white); flex: none; }

  .brand-name {
    font-size: 58px; font-weight: 700; letter-spacing: 1px;
    color: var(--silver); line-height: 1;
  }
  .web-address { font-size: 22px; color: var(--silver); letter-spacing: 0.3px; }
</style>
</head>
<body>

<article class="card card--front">
  <div class="band-top"></div>
  <div class="rule"></div>
  <section class="panel">
    <div class="holder">
      <h1 class="holder-name">Gordon Whitlock</h1>
      <p class="holder-address">482 Tarrow Lane<br>Suite 207<br>Larkfield, GA 30419</p>
    </div>
    <ul class="contact-list">
      <li class="contact-item">(770) 555-0142
        <svg class="contact-icon" viewBox="0 0 16 16"><path d="M3.6 1.2l2.3 2.6c.3.4.3.9 0 1.3L4.8 6.4c.9 1.9 2.9 3.9 4.8 4.8l1.3-1.1c.4-.3.9-.3 1.3 0l2.6 2.3c.4.4.4 1 0 1.4l-1.2 1.1C10.4 16.5 -.5 5.6 1.1 2.4L2.2 1.2c.4-.4 1-.4 1.4 0z"/></svg>
      </li>
      <li class="contact-item">(770) 555-0187
        <svg class="contact-icon" viewBox="0 0 16 16"><path d="M4 1h8a1 1 0 0 1 1 1v12a1 1 0 0 1-1 1H4a1 1 0 0 1-1-1V2a1 1 0 0 1 1-1zm.8 1.6v9.4h6.4V2.6zM8 12.6a.8.8 0 1 0 0 1.6.8.8 0 0 0 0-1.6z" fill-rule="evenodd"/></svg>
      </li>
      <li class="contact-item">bvel7kga@quellmail.com
        <svg class="contact-icon" viewBox="0 0 16 16"><path d="M1 3.5h14v9H1zM1.8 4.2 8 9l6.2-4.8" fill="none" stroke="#fff" stroke-width="1.3"/><path d="M1 3.5h14L8 8.6z"/></svg>
      </li>
      <li class="contact-item">www.bvel7kga.com
        <svg class="contact-icon" viewBox="0 0 16 16"><circle cx="8" cy="8" r="7"/><path d="M5 4.5c1.5.5 2 1.5 1.2 2.6-.8 1-.2 2 1 2.2.9.2.8 1.6.2 2.8M10.5 3c-.6 1.2.2 2 1.5 2" fill="none" stroke="#000" stroke-width="1.2"/></svg>
      </li>
    </ul>
  </section>
  <div class="rule"></div>
  <div class="band-bottom"></div>
</article>

<article class="card card--back">
  <div class="band-top"></div>
  <div class="rule"></div>
  <section class="panel">
    <span class="brand-name">BVEL7K</span>
  </section>
  <div class="rule"></div>
  <div class="band-bottom">
    <span class="web-address">www.bvel7kga.com</span>
  </div>
</article>

</body>
</html>
```